Flyer Design Project for Brightwater Wellbeing Rooms

We are a psychology clinic that specialises in eating, parenting and chronic illness & pain. See our website for a summary.

We need a flyer that will go to doctors and schools in the local area.

Things to include on the front page:

Immediate appointments available
After hours appointments available
Male and female psychologists

Phone 9563 2190
Web brightwaterwellbeingrooms.com.au

On the back page:

Phone 9563 2190
Suite 1/1287 Marlowe Rd, Kelverton East 3185.
brightwaterwellbeingrooms.com.au

Parenting: Parenthood is an amazing journey, but for lots of people it raises all sorts of issues from fear of birth, breastfeeding difficulties and settling problems, to toddler discipline and food fussiness all the way through to getting help for your depressed or anxious adolescent. Our Parenting Psychologists can help you be the best parent you can be which will in turn lead to happier families, homes, children and parents.

Chronic illness/pain: Diabetes, heart disease, arthritis, asthma, migraines, dizziness, chronic fatigue syndrome, infertility, and PCOS are just some of the conditions that can be managed with psychological interventions. Everything we do is about helping you to manage your condition and get back to focusing on what you really want your life to be about.

Eating: Whether you suffer from anorexia, bulimia or binge eating, our strategies help you develop a healthy relationship with food and your body. The practical tips and strategies that we can provide are very useful for people undergoing lapband surgery or liposuction.

I am interested in whether the photographs that I have already purchased can be used...so please have a look through the website and see which you think will suit your design. Photographs are not absolutely necessary though, so if it doesn't fit with your idea that is okay too.
Updates

HI Everyone,

Thanks for submitting so far! I haven't found anything yet that has hit the mark. And I am thinking that is my fault and maybe that way i have described what I want. I apologise and hope that this update might help.

This brochure is likely to sit with lots of other brochures in a doctors waiting room so it needs to be different - so that it will be noticed.

The majority of our market are women - so something feminine is important. Maybe it needs to be a little more playful that I had initially thought. Like maybe not your standard blocky text and bolds and primary colours. But something more creative, more personal.

I want to not focus just on the family theme. Parenting is one area that we cover, but also we help people with eating disorders and chronic illness/chronic pain. So the photographs that I use need to be more general. It is importnat to focus on happy and healthy looking people. As we went to appeal to what my potential clients want to look like and feel like.

I do hope this helps to guide you. I promise that once I see a flyer that I could choose, I will turn the funding to guaranteed. I did this last time...I am just a bit nervous as I haven't received anything yet that I am excited about.

Kindest regards,

Marnie.

Hi Everyone,

Thank you for your designs coming in! As promised, as soon as I received a design that I could see myself choosing I would change the status from refundable to committed. I have now done this!

I have received a design that I would say is good. It is not perfect however...so please keep the ideas coming.

To give more direction, the one that came in has a nice theme that runs through the brochure. Not too many different types of font and colours detracting from the flow of the flyer. However, the thing that I am concerned about is whether it will stand out enough on a rack of other flyers in a doctors waiting room.

I hope this helps with your creative ideas.

Thanks again to everyone!

Marnie.

Thanks SO much to everyone who is putting in designs. You are making my decision difficult!

I am wondering if you can update your designs with a few things:

can I ask you to make some text changes:

1. Can we have a heading on the front page: Psychologists  and then can you put Kelverton East in smaller writing just below it?

2. Id like to say on the front: Specialising in parenting, disordered eating and chronic pain & illness

3. Delete Male & Female Psychologists

4. In general we dont' need to have the logo standing out. We don't have a well known brand yet, so I am not wanting to take up valuable space with this - so perhaps it shoudl be small and maybe just on the back? Keeping the name of our clinic on the front with the website shoudl be sufficient.

Thanks heaps everyone...I will make decision very soon!

Target Market(s)

20-40 year olds. Working. Educated. Female. They might have a family/children.
Australian. Engish speaking.

Industry/Entity Type

Clinic

Requirements
Must have
• I would like to include our logo. Please do not use the colour green that it is in. I hate that colour! but I LOVE the logo.

I would like to follow through with some of the themes of the website and other stationary.

I will attach some of the other stationary I have had designed.

I really like the colours in the letterhead - especially that blue of the logo.

I think it needs to have a dash of colour with it at least...something that will stand out and be noticed on a brochure rack...but also have a look of class/sophistication/modern.
Nice to have
• Perhaps photograph of happy and healthy people.
Should not have
• I don't like bold text or too many different types of fonts.

It shouldn't look too cluttered so I might need to reduce the text I have included - I will need to see it first.

```html
<!DOCTYPE html>
<html lang="en">
<head>
<meta charset="utf-8">
<title>Brightwater Wellbeing Rooms – Flyer</title>
<link href="https://fonts.googleapis.com/css2?family=Josefin+Sans:wght@300;400&display=swap" rel="stylesheet">
<style>
  :root {
    --paper: #f1f1f3;
    --frame: #c9c9cc;
    --band-family: #6fa583;
    --band-health: #80c6c9;
    --band-exercise: #72aeaa;
    --band-lifestyle: #7e8a93;
    --ring: #6fb9bd;
    --brand-blue: #2eb0e4;
    --brand-grey: #6d6e71;
    --ink: #3a3a3c;
    --band-text: #ffffff;
  }
  html, body {
    margin: 0;
    padding: 0;
    overflow: hidden;
    background: var(--paper);
  }
  .flyer {
    position: relative;
    width: 1200px;
    height: 2565px;
    background: var(--paper);
    box-sizing: border-box;
    border: 3px solid var(--frame);
    overflow: hidden;
    font-family: "Josefin Sans", sans-serif;
    font-weight: 300;
  }
  .band {
    position: absolute;
    left: 0;
    width: 100%;
    height: 140px;
  }
  .band--family { top: 222px; background: var(--band-family); }
  .band--health { top: 590px; background: var(--band-health); }
  .band--exercise { top: 955px; background: var(--band-exercise); }
  .band--lifestyle { top: 1328px; background: var(--band-lifestyle); }
  .band__label {
    position: absolute;
    top: 50%;
    transform: translateY(-44%);
    margin: 0;
    color: var(--band-text);
    font-size: 66px;
    font-weight: 300;
    letter-spacing: 1px;
    line-height: 1;
  }
  .band--family .band__label { left: 846px; }
  .band--health .band__label { left: 228px; }
  .band--exercise .band__label { left: 832px; }
  .band--lifestyle .band__label { left: 222px; }

  .photo {
    position: absolute;
    width: 362px;
    height: 362px;
    border-radius: 50%;
    box-sizing: border-box;
    border: 8px solid var(--ring);
  }
  .photo--family {
    left: 141px; top: 107px;
    background: radial-gradient(circle at 60% 40%, #c99b7c 0%, #8aa35b 55%, #5c7e3a 100%);
  }
  .photo--health {
    left: 759px; top: 477px;
    background: linear-gradient(135deg, #e8a04d 0%, #f2c14a 35%, #d9544a 65%, #9fb25a 100%);
  }
  .photo--exercise {
    left: 141px; top: 842px;
    background: linear-gradient(120deg, #d8d8d6 0%, #b9b4ae 45%, #3e4652 75%, #c9c6c0 100%);
  }
  .photo--lifestyle {
    left: 759px; top: 1216px;
    background: linear-gradient(180deg, #4f8fd6 0%, #8ab9ea 55%, #7aa64a 85%, #5e8b35 100%);
  }

  .brand {
    position: absolute;
    left: 290px;
    top: 1730px;
    display: flex;
    align-items: center;
    gap: 44px;
  }
  .brand__dot {
    width: 190px;
    height: 190px;
    border-radius: 50%;
    background: var(--brand-blue);
  }
  .brand__name {
    margin: 0;
    color: var(--brand-grey);
    font-size: 44px;
    font-weight: 400;
    letter-spacing: 7px;
    line-height: 60px;
    text-transform: uppercase;
  }

  .details {
    position: absolute;
    left: 0;
    top: 2082px;
    width: 100%;
    margin: 0;
    padding: 0;
    list-style: none;
    text-align: center;
    color: var(--ink);
    font-size: 36px;
    font-weight: 300;
    line-height: 75px;
  }
</style>
</head>
<body>
  <main class="flyer">
    <section class="band band--family"><h2 class="band__label">Family</h2></section>
    <section class="band band--health"><h2 class="band__label">Health</h2></section>
    <section class="band band--exercise"><h2 class="band__label">Exercise</h2></section>
    <section class="band band--lifestyle"><h2 class="band__label">Lifestyle</h2></section>

    <div class="photo photo--family" role="img" aria-label="Photo of a mother playing with her toddler on grass"></div>
    <div class="photo photo--health" role="img" aria-label="Photo of fresh sliced fruit: orange, kiwi and melon"></div>
    <div class="photo photo--exercise" role="img" aria-label="Photo of a woman exercising with hand weights"></div>
    <div class="photo photo--lifestyle" role="img" aria-label="Photo of a woman riding a bicycle under a blue sky"></div>

    <div class="brand">
      <div class="brand__dot"></div>
      <h1 class="brand__name">Brightwater<br>Wellbeing<br>Rooms</h1>
    </div>

    <ul class="details">
      <li>Immediate appointments available</li>
      <li>After hours appointments available</li>
      <li>Male and female psychologists</li>
      <li>Phone 9563 2190</li>
      <li>Web brightwaterwellbeingrooms.com.au</li>
    </ul>
  </main>
</body>
</html>
```